Refresh of far beyond ordinary IT house website

Our web site is starting to show it's age. You can see the existing site here: www.plumbrook.net. As a growing company we want to come across as a dynamic collection of IT experts.

We want to update the design so are open to any colour palette and look, but want to retain our current table logo. We use the logo on our business cards but with a white background - see the attached file, so you don't need to keep the brown or the green.

The design should consider the range of browsers that will be looking at the site - so please show how it will look on a wide screen laptop and a 768x1024 tablet.

We want to add some pages about our team and their skills, probably with photos of each person on the team.

This is an uncoded project - the PSD files of the design is required, not coding.
Updates

Thanks everyone for the submissions so far.  It's a holiday day in the UK today but we will get some feedback on the designs so far out to you.

Target Market(s)

Architects and other creative types looking for IT support

Industry/Entity Type

Business

Font styles to use
Serif
Sans Serif

Requirements
Must have
• Must look good on a laptop and an iPad.

```html
<!DOCTYPE html>
<html lang="en">
<head>
<meta charset="utf-8">
<title>plumbrook – IT Support</title>
<link href="https://fonts.googleapis.com/css2?family=Oxygen:wght@400;700&family=Oswald:wght@400;500&display=swap" rel="stylesheet">
<style>
:root{
  --plum:#8c1150;
  --plum-dark:#6a0b3d;
  --gold:#d4a800;
  --ink:#333;
  --text:#444;
  --grey-band:#ececec;
  --line:#d8d8d8;
  --white:#fff;
}
*{box-sizing:border-box;margin:0;padding:0}
html,body{width:974px;height:1200px;overflow:hidden}
body{position:relative;background:var(--white);font-family:'Oxygen',sans-serif;color:var(--text)}
.abs{position:absolute}
.top-rule{left:0;top:0;width:974px;height:4px;background:var(--gold)}
.header{left:0;top:4px;width:974px;height:97px;background:linear-gradient(#fff,#f2f2f2);border-bottom:1px solid #ddd}
.brand{left:108px;top:16px;display:flex;align-items:center;gap:12px}
.brand-mark{width:40px;height:40px;background:var(--gold)}
.brand-name{font-size:40px;font-weight:700;color:var(--plum);letter-spacing:-.5px}
.chat-badge{left:729px;top:15px;width:131px;height:50px;border:1px solid #ccc;border-radius:4px;background:#fff;display:flex;align-items:center}
.chat-agent{width:38px;height:48px;background:linear-gradient(#e9d7cb,#cfc4bd)}
.chat-text{font-family:'Oswald',sans-serif;font-size:16px;line-height:21px;padding-left:6px}
.chat-text .a{color:var(--plum)}.chat-text .b{color:#1f7a16}
.nav{left:296px;top:78px;display:flex;gap:0;font-size:12px;font-weight:700;text-transform:uppercase}
.nav a{color:var(--plum);text-decoration:none;padding:4px 8px 3px;display:block}
.nav a.active{background:#333;color:#fff;font-size:13px}
.hero{left:0;top:101px;width:974px;height:361px;background:linear-gradient(135deg,#c9c6d6 0%,#dcd8e4 40%,#b9b4c6 75%,#4a4650 100%)}
.hero-caption{left:0;top:426px;width:974px;height:34px;background:rgba(40,40,40,.75);border-bottom:3px solid #333}
.hero-caption span{position:absolute;left:0;right:0;text-align:center;font-family:'Oswald',sans-serif;font-size:24px;color:#fff;top:0;line-height:34px}
.dots{left:771px;top:436px;display:flex;gap:9px}
.dots i{width:14px;height:14px;border-radius:50%;background:var(--gold)}
.dots i:first-child{background:#fff}
.heading{left:0;width:974px;text-align:center;font-size:27px;font-weight:700;color:var(--ink)}
.heading em{font-style:normal;color:var(--plum)}
.heading svg{vertical-align:middle}
.about-text{left:120px;top:514px;width:734px;text-align:center;font-size:11px;line-height:17px}
.more{left:0;top:588px;width:974px;text-align:center;font-size:12px;font-weight:700;color:var(--plum)}
.services{left:0;top:607px;width:974px;height:218px;background:var(--grey-band);border-top:1px solid #ddd;border-bottom:1px solid #ddd}
.service{position:absolute;top:59px;width:130px;text-align:center;font-size:12px;font-weight:700;color:var(--ink)}
.service .ring{width:90px;height:90px;margin:0 auto 16px;border:4px solid var(--gold);border-radius:50%;background:#fff;display:flex;align-items:center;justify-content:center}
.col{top:852px;width:230px}
.col-title{font-size:18px;font-weight:700;color:var(--ink);padding-bottom:6px;border-bottom:2px solid #ddd;display:flex;align-items:center;gap:7px}
.col-title em{font-style:normal;color:var(--plum)}
.news-item{font-size:10px;line-height:14px;padding:12px 0 5px;border-bottom:1px dashed #ccc}
.news-item b{display:block;font-size:11px;margin-bottom:4px;color:var(--ink)}
.news-item:last-of-type{border:0}
.read{font-size:11px;font-weight:700;color:var(--plum);text-align:right;margin-top:6px}
.quote{margin-top:14px;background:#eee;border-radius:8px;padding:12px 10px 30px 16px;font-style:italic;font-size:11px;line-height:17px;color:#555}
.client{display:flex;align-items:center;gap:14px;margin-top:-22px;padding-left:16px}
.client-photo{width:54px;height:54px;border:2px solid #fff;background:linear-gradient(#8aa1b1,#2c3844)}
.client b{font-size:10px;color:var(--ink);margin-top:20px}
.field{margin-top:10px;border:1px solid #bbb;border-radius:3px;height:23px;font-size:10px;font-style:italic;color:#777;padding:5px 8px}
.field.msg{height:58px}
.submit{margin-top:13px;display:inline-block;background:var(--plum-dark);color:#fff;font-size:12px;font-weight:700;padding:3px 8px;border-radius:2px}
.footer{left:0;top:1075px;width:974px;height:125px;background:linear-gradient(var(--plum),var(--plum-dark));border-top:2px solid var(--gold);color:#fff}
.fbox{position:absolute;top:16px;height:62px;border:1px solid rgba(255,255,255,.25);background:rgba(255,255,255,.07);padding:6px 10px}
.fbox h4{font-size:12px;margin-bottom:7px}
.f-input{display:inline-block;width:146px;height:22px;background:rgba(255,255,255,.2);font-size:10px;font-style:italic;padding:5px 8px}
.f-go{display:inline-block;width:25px;height:22px;background:#3a0a22;vertical-align:top;margin-left:6px;text-align:center;line-height:22px;font-weight:700}
.f-line{font-size:10px;display:flex;align-items:center;gap:8px;margin-top:3px}
.socials{display:flex;gap:11px;margin-top:9px}
.socials i{width:20px;height:20px;border-radius:3px;background:rgba(255,255,255,.55)}
.foot-brand{left:648px;top:30px;display:flex;align-items:center;gap:10px;font-size:29px;font-weight:700;color:rgba(255,255,255,.85)}
.foot-brand span{width:36px;height:30px;background:rgba(255,255,255,.45)}
.foot-links{left:115px;top:98px;font-size:10px}
.foot-copy{left:666px;top:98px;font-size:10px}
</style>
</head>
<body>
<div class="abs top-rule"></div>
<header class="abs header"></header>
<div class="abs brand"><span class="brand-mark"></span><span class="brand-name">plumbrook</span></div>
<div class="abs chat-badge"><div class="chat-agent" role="img" aria-label="Support agent wearing a headset"></div><div class="chat-text"><span class="a">LIVE CHATT</span><br><span class="b">AVAILABLE</span></div></div>
<nav class="abs nav"><a class="active">Home</a><a>About Us</a><a>What We Do</a><a>News Blog</a><a>Articles</a><a>Clients</a><a>Partners</a><a>Contact Us</a></nav>

<div class="abs hero" role="img" aria-label="Architectural blueprints with pencils, a marker, compasses and a calculator"></div>
<div class="abs hero-caption"><span>Serious IT Support For Business</span></div>
<div class="abs dots"><i></i><i></i><i></i><i></i></div>

<div class="abs heading" style="top:474px">
<svg width="210" height="12"><path d="M0 6H210M40 3H205M60 9H200" stroke="#555" stroke-width="1.2"/></svg>
About <em>plumbrook</em>
<svg width="210" height="12"><path d="M0 6H210M5 3H170M10 9H150" stroke="#555" stroke-width="1.2"/></svg>
</div>
<p class="abs about-text">Plumbrook was established with a specific aim: to consistently deliver an advanced and comprehensive IT service for ambitious growing companies across many industry sectors. We aim to provide the very best in service and support, and to aid business growth through the effective and skilled use of modern IT solutions. Founded in 2003, we have grown rapidly and have delivered successful business solutions to small and medium sized businesses, working with customers across a wide IT spectrum. The knowledge...</p>
<div class="abs more">More +</div>

<section class="abs services">
  <div class="abs heading" style="top:17px">
  <svg width="210" height="12"><path d="M0 6H210M40 3H205M60 9H200" stroke="#555" stroke-width="1.2"/></svg>
  Our <em>Services</em>
  <svg width="210" height="12"><path d="M0 6H210M5 3H170M10 9H150" stroke="#555" stroke-width="1.2"/></svg>
  </div>
  <div class="service" style="left:125px"><div class="ring"><svg width="50" height="60" viewBox="0 0 50 60" fill="none" stroke="#8c1150" stroke-width="4"><circle cx="25" cy="18" r="15"/><path d="M18 12c2 8 6 12 14 14" stroke-width="5"/><path d="M25 33v8"/><ellipse cx="26" cy="50" rx="8" ry="6" fill="#8c1150"/></svg></div>It Support &amp; Management</div>
  <div class="service" style="left:278px"><div class="ring"><svg width="56" height="50" viewBox="0 0 56 50"><path d="M12 36a10 10 0 0 1 2-20a14 14 0 0 1 27-3a11 11 0 0 1 4 23z" fill="#8c1150"/><path d="M20 44l14-14M26 30h8v8" stroke="#fff" stroke-width="3" fill="none"/></svg></div>Cloud Computing</div>
  <div class="service" style="left:432px"><div class="ring"><svg width="52" height="52" viewBox="0 0 52 52"><rect x="4" y="4" width="44" height="44" rx="6" fill="#8c1150"/><rect x="12" y="14" width="28" height="18" fill="#fff"/><rect x="18" y="36" width="16" height="4" fill="#fff"/></svg></div>Disaster Recovery</div>
  <div class="service" style="left:577px"><div class="ring"><svg width="52" height="52" viewBox="0 0 52 52"><path d="M26 4l20 9v18l-20 17L6 31V13z" fill="#8c1150"/><path d="M6 13l20 9 20-9M26 22v26" stroke="#fff" stroke-width="2" fill="none"/></svg></div>Virtualisation</div>
  <div class="service" style="left:724px"><div class="ring"><svg width="52" height="56" viewBox="0 0 52 56" stroke="#8c1150" stroke-width="4" fill="none"><circle cx="26" cy="8" r="4"/><path d="M24 12L10 50M28 12l14 38M12 32h28"/></svg></div>CAD Services</div>
</section>

<div class="abs col" style="left:115px">
  <div class="col-title"><svg width="20" height="18"><path d="M2 6h5l9-5v16L7 12H2z" fill="#555"/></svg>Latest <em>News</em></div>
  <div class="news-item"><b>04/17/2014</b>Lorem ipsum dolor sit amet, cctetuer adipiscingin elit, sed diam nummy nibh eui smod tinciduntiotvulputate velit esse olestie</div>
  <div class="news-item"><b>04/17/2014</b>Lorem ipsum dolor sit amet, cctetuer adipiscingin elit, sed diam nummy nibh eui smod tinciduntiotvulputate velit esse olestie</div>
  <div class="read">Read more »</div>
</div>
<div class="abs col" style="left:372px">
  <div class="col-title"><svg width="20" height="18"><rect x="1" y="2" width="13" height="9" rx="2" fill="#555"/><rect x="7" y="7" width="12" height="9" rx="2" fill="#555"/></svg>Client <em>Testimonial</em></div>
  <div class="quote">Duis autem vel eum iriureol hder in vultat velit esse moles conqat vela ilu dolor feugiat.Duis autem vel eum ure hendrern vultat velit esse autm vel eum</div>
  <div class="client"><div class="client-photo" role="img" aria-label="Client portrait"></div><b>Mr. Dolore Eu Feugiat</b></div>
  <div class="read" style="margin-top:-4px">Read more »</div>
</div>
<div class="abs col" style="left:630px">
  <div class="col-title"><svg width="18" height="18"><path d="M2 2h9v14H2z" fill="none" stroke="#555" stroke-width="2"/><path d="M9 12l7-7" stroke="#555" stroke-width="3"/></svg>Quick <em>Contact</em></div>
  <div class="field">Name</div>
  <div class="field">Email</div>
  <div class="field msg">Message</div>
  <div class="submit">Submit</div>
</div>

<footer class="abs footer">
  <div class="fbox" style="left:115px;width:199px"><h4>Subscribe to Newsletter</h4><span class="f-input">Email here</span><span class="f-go">›</span></div>
  <div class="fbox" style="left:337px;width:130px"><h4>Contact Us</h4>
    <div class="f-line"><svg width="10" height="10"><path d="M2 1l3 2-1 2 2 2 2-1 2 3-2 1C5 10 0 5 1 2z" fill="#d9a"/></svg>012-345-6789</div>
    <div class="f-line"><svg width="10" height="8"><rect x=".5" y=".5" width="9" height="7" fill="none" stroke="#d9a"/><path d="M.5 .5l4.5 4 4.5-4" stroke="#d9a" fill="none"/></svg>info@plumbrook.net</div>
  </div>
  <div class="fbox" style="left:490px;width:96px"><h4>Follow Us</h4><div class="socials" aria-label="Social links"><i></i><i></i><i></i></div></div>
  <div class="abs foot-brand"><span></span>plumbrook</div>
  <div class="abs foot-links">Home &nbsp;|&nbsp; About Us &nbsp;|&nbsp; What we do &nbsp;|&nbsp; News Blog &nbsp;|&nbsp; Articles &nbsp;|&nbsp; Clients &nbsp;|&nbsp; Partners &nbsp;|&nbsp; Terms &nbsp;|&nbsp; Support &nbsp;|&nbsp; Contact</div>
  <div class="abs foot-copy">© 2014 plumbrook. All Rights Reserved.</div>
</footer>
</body>
</html>
```